Business Card Design

Hello,
I try and keep my business card fresh and current. So about every year i get a new one. This year I'd like something with a white background and black lettering.
Before you start - I do not want my phone number or any other description on the card other than my url and my email.

I'd like a double sided business card with
TedMarlow.com on one side

and

Ted@TedMarlow.com on the other side of the card

Thinking very minimalistic and modern.
I don't have a particular font i mind or how to capitalize my name or website. This card will lead people to my new website that is being designed to showcase my photography and music.

* Initial thought was the front side of the card having a grid-like pattern built out of dashes or periods, with my website sitting within the pattern and on the back side my email on a stark white background. But that might look completely lame - haha.

I'm looking forward to seeing what you come up with.

thank you,
- ted marlow

Reason: Want to spend some more time with the designs and add a little $. thanks for all the designs - ted

Wanted to add a little $ and spend some more time with the designs.

big thanks to all who have submitted work 

- ted

www.tedmarlow.com
ted@tedmarlow.com

000000
ffffff

• tedmarlow.com
ted@tedmarlow.com
• phone number
any description of what i do, photography or music

```html
<!DOCTYPE html>
<html lang="en">
<head>
<meta charset="utf-8">
<title>Ted Marlow — Business Card</title>
<link rel="stylesheet" href="https://fonts.googleapis.com/css2?family=Jost:wght@400&display=swap">
<style>
  :root {
    --ink: #000000;
    --paper: #ffffff;
    --backdrop: #e4e4e4;
    --dot-tone-light: #ffffff;
    --dot-tone-deep: #ebebeb;
    --card-shadow: rgba(0, 0, 0, 0.12);
  }

  * { box-sizing: border-box; margin: 0; padding: 0; }

  html, body {
    width: 1200px;
    height: 1200px;
    overflow: hidden;
  }

  body {
    background: var(--backdrop);
    font-family: "Jost", "Futura", sans-serif;
    color: var(--ink);
    display: flex;
    flex-direction: column;
    align-items: center;
    justify-content: center;
    gap: 60px;
  }

  .card {
    position: relative;
    width: 840px;
    height: 480px;
    background: var(--paper);
    box-shadow: 0 6px 24px var(--card-shadow);
    overflow: hidden;
  }

  .card__text {
    position: absolute;
    font-weight: 400;
    letter-spacing: 0.01em;
    line-height: 1;
    white-space: nowrap;
  }

  /* Back: email on stark white */
  .card--email .card__text {
    top: 96px;
    left: 84px;
    font-size: 30px;
  }

  /* Front: website set within the dot grid */
  .card--web .dot-field {
    position: absolute;
    inset: 0;
    background: linear-gradient(135deg, var(--dot-tone-light) 0%, var(--dot-tone-deep) 45%, var(--dot-tone-deep) 100%);
  }

  .card--web .card__text {
    right: 96px;
    bottom: 72px;
    font-size: 32px;
  }
</style>
</head>
<body>
  <section class="card card--email" aria-label="Business card back">
    <p class="card__text">Ted@TedMarlow.com</p>
  </section>

  <section class="card card--web" aria-label="Business card front">
    <div class="dot-field" role="img" aria-label="Fine black dot grid pattern covering the card"></div>
    <p class="card__text">TedMarlow.com</p>
  </section>
</body>
</html>
```